Webbanner-Design für Fachhandel für Medizinprodukte
Zielgruppe
wir sind ein Fachhandel für Medizinprodukte.
Aufgabenstellung
-Slider / Banner
-1920 x 340
-Es muss ein intersannter Satz auf dem Bild sein, der einläd zu klicken.
-https://www.veloquar-beispiel.de/
- folgender Artikel soll beworben werden:
-https://www.veloquar-beispiel.de/fingerpulsoximeter-kt508-pulsoximeter-weiss-4186
-Design soll gut zur Seite passen.
-Das Bild kann von der Seite verwendet werden.
-Gerne können zusätzlich auch Stockbilder verarbeitet werden.

```html
<!DOCTYPE html>
<html lang="de">
<head>
<meta charset="utf-8">
<title>Entspannt messen – Banner-Varianten</title>
<link rel="stylesheet" href="https://fonts.googleapis.com/css2?family=Arimo:wght@700&display=swap">
<style>
  :root {
    --stage: #9ba0a4;
    --green: #45ae4b;
    --green-soft: #7cc482;
    --green-pale: #b9e0bc;
    --panel: #e1e1e1;
    --panel-light: #f1f1f1;
    --white: #ffffff;
    --rule: #c4c4c4;
  }
  html, body {
    margin: 0;
    width: 1200px;
    height: 1200px;
    overflow: hidden;
    background: var(--stage);
  }
  .stage {
    position: relative;
    width: 1200px;
    height: 1200px;
  }
  .banner {
    position: absolute;
    left: 76px;
    width: 1056px;
    display: block;
  }
  .banner--wave { top: 154px; }
  .banner--circle { top: 523px; }
  .banner--facet { top: 881px; }
  .headline {
    font-family: "Arimo", Arial, sans-serif;
    font-weight: 700;
    font-size: 125px;
  }
  .headline--white { fill: var(--white); }
  .headline--green { fill: var(--green); }
</style>
</head>
<body>
<main class="stage">

  <!-- Variante 1: grüne Welle -->
  <svg class="banner banner--wave" viewBox="0 0 1700 300" aria-label="Entspannt messen">
    <defs>
      <linearGradient id="device-fill" x1="0" y1="0" x2="0" y2="1">
        <stop offset="0" stop-color="#fafafa"/>
        <stop offset="1" stop-color="#dadada"/>
      </linearGradient>
      <symbol id="plus-badge" viewBox="0 0 56 56">
        <rect width="56" height="56" rx="12" fill="var(--green)"/>
        <rect x="21" y="10" width="14" height="36" rx="5" fill="var(--white)"/>
        <rect x="10" y="21" width="36" height="14" rx="5" fill="var(--white)"/>
      </symbol>
    </defs>
    <rect class="banner__bg" width="1700" height="300" fill="var(--panel)"/>
    <path class="banner__band" fill="var(--green)"
          d="M0 0 H1700 V218 L1322 292 C1100 270 850 258 700 248 C520 236 330 220 150 196 L0 187 Z"/>
    <rect class="product-photo" role="img" aria-label="Weißes Fingerpulsoximeter, Vorderansicht mit Display"
          x="150" y="40" width="180" height="250" rx="26" fill="url(#device-fill)"
          transform="rotate(-16 240 165)"/>
    <rect class="product-photo" role="img" aria-label="Weißes Fingerpulsoximeter, Seitenansicht"
          x="400" y="46" width="304" height="224" rx="26" fill="url(#device-fill)"
          transform="rotate(-4 552 158)"/>
    <use href="#plus-badge" x="10" y="258" width="32" height="32"/>
    <text class="headline headline--white" x="878" y="108" textLength="745" lengthAdjust="spacing">ENTSPANNT</text>
    <text class="headline headline--white" x="878" y="238" textLength="515" lengthAdjust="spacing">MESSEN</text>
  </svg>

  <!-- Variante 2: Kreisform -->
  <svg class="banner banner--circle" viewBox="0 0 1688 298" aria-label="Entspannt messen">
    <defs>
      <clipPath id="circle-clip"><rect width="1688" height="298"/></clipPath>
    </defs>
    <rect class="banner__bg" width="1688" height="298" fill="var(--panel)"/>
    <g clip-path="url(#circle-clip)">
      <circle cx="1150" cy="238" r="140" fill="var(--panel-light)"/>
      <circle cx="1398" cy="143" r="235" fill="var(--green)"/>
      <circle cx="1690" cy="150" r="140" fill="var(--green-soft)" opacity="0.85"/>
      <circle cx="1610" cy="270" r="74" fill="var(--green-pale)"/>
    </g>
    <rect class="product-photo" role="img" aria-label="Weißes Fingerpulsoximeter, Seitenansicht"
          x="1246" y="40" width="300" height="222" rx="26" fill="url(#device-fill)"
          transform="rotate(-4 1396 151)"/>
    <text class="headline headline--green" x="36" y="128" textLength="737" lengthAdjust="spacing">ENTSPANNT</text>
    <line x1="36" y1="149" x2="773" y2="149" stroke="var(--rule)" stroke-width="3"/>
    <text class="headline headline--white" x="36" y="258" textLength="508" lengthAdjust="spacing">MESSEN</text>
    <use href="#plus-badge" x="561" y="203" width="57" height="57"/>
  </svg>

  <!-- Variante 3: Facetten -->
  <svg class="banner banner--facet" viewBox="0 0 1700 308" aria-label="Entspannt messen">
    <rect class="banner__bg" width="1700" height="308" fill="var(--panel)"/>
    <polygon class="banner__facet" fill="var(--green)"
             points="78,0 230,0 612,168 655,222 288,308 30,308"/>
    <polyline fill="none" stroke="var(--white)" stroke-width="3" points="230,0 658,125 390,308"/>
    <line x1="38" y1="0" x2="0" y2="265" stroke="var(--white)" stroke-width="3"/>
    <line x1="0" y1="218" x2="32" y2="0" stroke="var(--green)" stroke-width="3"/>
    <line x1="290" y1="308" x2="658" y2="225" stroke="var(--green)" stroke-width="3"/>
    <rect class="product-photo" role="img" aria-label="Weißes Fingerpulsoximeter, Seitenansicht"
          x="86" y="34" width="350" height="250" rx="28" fill="url(#device-fill)"
          transform="rotate(-6 261 159)"/>
    <text class="headline headline--green" x="846" y="132" textLength="746" lengthAdjust="spacing">ENTSPANNT</text>
    <text class="headline headline--white" x="846" y="267" textLength="513" lengthAdjust="spacing">MESSEN</text>
    <use href="#plus-badge" x="1380" y="214" width="57" height="57"/>
  </svg>

</main>
</body>
</html>
```